Website: Orvalink Business Consultants, Qianhai SEZ, China

Our client is a business consultancy firm and will be the first to set up in the Qianhai Shenzhen-Hong Kong Modern Service Industry Cooperation Zone, China So we need a corporate website concept that engages service, finance and technology sector companies. The company can provide all the necessary services needed to set up shop in Qianhai. They are looking for a modern, international, reliable and strong image.

Here are some websites for reference prupose:

http://www.brenwickpartners.example/ (we like the dynamic banner and clear, clean layout of this website)

http://www.dovetrassadvisory.example/ (we like the background city image, use of light font, hover over menu functions and color scheme - purple and grey)

http://www.pelmo.example/ (we like the simplicity of this website, clear lines and we like the dynamic banner)
Updates

Hello, We are currently undecided between three logo designs.  All three have been uploaded to the design brief so that you can use them as reference for the website design. Thx

Also please take note of the addition menu selection 'About Qianhai'. Thx

Hello all Designers, First of all we want thank you for participating in our website competition, the calibre of design was high and we appreciated the expedience. Our company is Quillon Reach Web Design and Internet Marketing based in Shenzhen, China. We anticipate rapid growth in the Chinese domestic market as the country shifts in to a service sector economy. We hope to continue building reliable working relationships with you based on idea sharing and constructive feedback. Once again, Thankyou, QR Team

Target Market(s)

International finance and technology companies looking to set up in Qianhai Special Economic Zone, China

Industry/Entity Type

Finance

Requirements
Must have
• Initial design for home page and in later selection stages a secondary page will be required.

The design should be for PSD concepts only no code!

Menu bar, Photo banner -
A. Photo banner and text overlay,
B.Photo Banner and text description to left or right.

Social Connect icons, Site search bar (top right), Logo space (top left).

Menu bar at top with Home, About Us, About Qianhai, Services, Portfolio, Partners, Our Team Contact Us.

Standard 3-4 box layout - Banner at top and 2-3 boxes under banner.

Colour scheme- A. Purple and Blue, must have light background/body
B. Shades of white, black and grey.

Simple, clear, clean, sharp.

```html
<!DOCTYPE html>
<html lang="en">
<head>
<meta charset="utf-8">
<title>Orvalink Business Consultants</title>
<link rel="stylesheet" href="https://fonts.googleapis.com/css2?family=Ubuntu:wght@400;500;700&family=Jost:wght@400;500&display=swap">
<style>
:root{
  --page:#f2f2f2;
  --white:#ffffff;
  --ink:#3c3c3c;
  --text:#666666;
  --muted:#8a8a8a;
  --magenta:#c4168c;
  --blue:#1a94d2;
  --rule:#cfcfcf;
  --nav-top:#a3a3a3;
  --nav-bottom:#7b7b7b;
}
*{box-sizing:border-box;margin:0;padding:0}
html,body{width:1200px;height:1200px;overflow:hidden}
body{position:relative;background:var(--page);font-family:"Ubuntu",sans-serif;color:var(--text)}
.abs{position:absolute}

.site-header{left:0;top:0;width:1200px;height:147px;background:linear-gradient(#ffffff,#f0f0f0)}
.brand{left:116px;top:62px}
.brand-name{font-family:"Ubuntu",sans-serif;font-size:27px;letter-spacing:4px;color:#2f2f2f;font-weight:400;display:flex;align-items:center;gap:10px}
.brand-dot{width:14px;height:14px;border-radius:50%;background:var(--magenta)}
.brand-tag{font-size:10px;letter-spacing:1.6px;color:#333;margin-top:6px;padding-left:54px}
.call{right:112px;top:43px;font-size:21px;color:#8a8a8a;font-weight:400}
.search{left:853px;top:83px;width:236px;height:32px;border:1px solid #d2d2d2;border-radius:5px;background:#fff;box-shadow:inset 0 1px 3px rgba(0,0,0,.08)}
.search svg{position:absolute;right:10px;top:9px}

.main-nav{left:0;top:147px;width:1200px;height:43px;background:linear-gradient(var(--nav-top),var(--nav-bottom))}
.main-nav ul{list-style:none;display:flex;position:absolute;left:94px;top:0;height:43px;align-items:center}
.main-nav li{color:#fff;font-size:14px;padding:0 25px;border-right:1px solid rgba(255,255,255,.55);height:22px;line-height:22px;margin-top:0}
.main-nav li:last-child{border-right:none}

.hero{left:109px;top:219px;width:977px;height:356px;background:var(--white);border:1px solid #dcdcdc}
.hero-photo{position:absolute;left:405px;top:5px;width:565px;height:344px;background:linear-gradient(90deg,#ffffff 0%,#e9e9e9 20%,#c9c9c9 55%,#a9a9a9 80%,#c4c4c4 100%)}
.hero h1{position:absolute;left:21px;top:56px;font-family:"Jost",sans-serif;font-weight:500;font-size:20px;letter-spacing:1px;color:#333}
.hero ul{position:absolute;left:22px;top:96px;list-style:none;font-size:12.5px;color:#666}
.hero li{height:26px;line-height:18px}
.hero li::before{content:"";display:inline-block;width:5px;height:5px;border-radius:50%;background:#444;margin-right:9px;vertical-align:2px}
.hero .more{position:absolute;left:34px;top:260px;font-size:14px;color:var(--blue);font-family:Arial,sans-serif}

.intro-title{left:114px;top:614px;font-size:15px;font-weight:500;color:var(--magenta);letter-spacing:.3px}
.intro-text{left:113px;top:642px;width:580px;font-size:12.5px;line-height:20px;color:#6b6b6b}
.intro-text a{color:var(--blue);text-decoration:none}
.dotted{height:0;border-top:1px dotted #b9b9b9}

.news-thumb{width:136px;height:134px;background:#fff;border:1px solid #e0e0e0;padding:3px}
.news-thumb div{width:100%;height:100%;background:linear-gradient(160deg,#e6ecef 0%,#b9c3c8 45%,#5b6064 100%)}
.news{left:259px;width:440px}
.news .meta{font-size:11px;font-weight:700;color:var(--magenta);letter-spacing:.4px}
.news .meta span{color:#999;margin-left:10px}
.news h3{font-size:13px;font-weight:500;color:#444;margin-top:8px}
.news p{font-size:11.5px;line-height:18px;color:#666;margin-top:5px}
.news .offer{font-size:11.5px;color:#555;margin-top:9px}
.news .offer b{font-weight:400;color:var(--blue)}

.tile{background:#fff;border:1px solid #d8d8d8;padding:3px}
.tile div{width:100%;height:100%}
.caption{font-size:12.5px;color:#555}

.pubs-title{left:733px;top:953px;font-size:16.5px;color:#444;letter-spacing:.3px}
.pubs{left:733px;top:986px;list-style:none;font-size:11.5px;color:#444;letter-spacing:.2px}
.pubs li{height:24px}
.pubs li::before{content:"";display:inline-block;width:5px;height:5px;border-radius:50%;background:#444;margin-right:8px;vertical-align:2px}
.pubs b{font-weight:400;color:var(--blue)}

.footer-links{left:113px;top:1152px;font-family:Arial,sans-serif;font-size:12px;color:#555}
.copyright{right:114px;top:1151px;font-family:Arial,sans-serif;font-size:12px;color:#555}
</style>
</head>
<body>

<header class="site-header abs">
  <div class="brand abs">
    <div class="brand-name"><span class="brand-dot"></span>ORVALINK</div>
    <div class="brand-tag">BUSINESS CONSULTING</div>
  </div>
  <div class="call abs">call us: &nbsp;+1 555 014 2290</div>
  <div class="search abs">
    <svg width="12" height="12" viewBox="0 0 12 12"><circle cx="5" cy="5" r="3.6" fill="none" stroke="#333" stroke-width="1.4"/><line x1="7.6" y1="7.6" x2="11" y2="11" stroke="#333" stroke-width="1.8"/></svg>
  </div>
</header>

<nav class="main-nav abs">
  <ul>
    <li>Home</li><li>About Us</li><li>About Qianhai</li><li>Services</li><li>Portfolio</li><li>Partners</li><li>Our Team</li><li>Contact Us</li>
  </ul>
</nav>

<section class="hero abs">
  <div class="hero-photo" role="img" aria-label="Photo of a team of consultants working together at an office table"></div>
  <h1>SIMPLY DUMMY TEXT OF THE PRINTING</h1>
  <ul>
    <li>Lorem Ipsum has been the industry's standard dummy.</li>
    <li>since the 1500s, when an unknown printer took a galley.</li>
    <li>Scrambled it to make a type specimen book.</li>
    <li>It has survived not only five centuries, but also the leap</li>
    <li>Typesetting, remaining essentially unchanged was popularised</li>
    <li>With the release of Letraset sheets containing</li>
  </ul>
  <div class="more">More Details...</div>
</section>

<h2 class="intro-title abs">Lorem ipsum dolor sit amet consecdi.</h2>
<p class="intro-text abs">Scing elraesent ves tibm moeaean onummy hendrerit mauris. Phasellus portauspit varius miso-<br>ciis ulus mus. Nulla dui. Fusce feugiat malesuada odio. Morbi nio gravida atcursus necuus a<br>loreenas tristique orci ac sem. Duis ultricies pharetra magna. Donec acumsan<br>malesuada orcinec sit amet eros. Lorem ipsum dolor sit am consectetuer adipiscing eliuris<br>fermentum dictum magna. Sed oreet aliquam leo. <a>[+].</a></p>

<div class="dotted abs" style="left:113px;top:762px;width:536px"></div>

<div class="news-thumb abs" style="left:113px;top:780px" role="img" aria-label="Photo of a businessman presenting to colleagues"><div></div></div>
<article class="news abs" style="top:786px">
  <div class="meta">ENERGY &amp; UTILITIES<span>APRIL 2013</span></div>
  <h3>Restructuring Debts of Discoms' for Sustainable Power Growth</h3>
  <p>India is fast catching up and the availability of power has a huge impact on the economic growth. In the last years, the country has massively enlarged its power India faces the challenge....</p>
  <div class="offer"><b>SERVICES OFFERED</b> The new face of competition</div>
</article>

<div class="dotted abs" style="left:113px;top:933px;width:536px"></div>

<div class="news-thumb abs" style="left:115px;top:965px" role="img" aria-label="Photo of a businessman presenting to colleagues"><div></div></div>
<article class="news abs" style="top:970px">
  <div class="meta">ENERGY &amp; UTILITIES<span>APRIL 2013</span></div>
  <h3>Restructuring Debts of Discoms' for Sustainable Power Growth</h3>
  <p>India is fast catching up and the availability of power has a huge impact on the economic growth. In the last years, the country has massively enlarged its power&nbsp; India faces the challenge...</p>
  <div class="offer"><b>SERVICES OFFERED</b> The new face of competition</div>
</article>

<div class="tile abs" style="left:732px;top:619px;width:130px;height:114px"><div role="img" aria-label="Image of a green balloon" style="background:radial-gradient(circle at 65% 45%,#7cc04a,#2f6a1e 45%,#cfd6d8 75%)"></div></div>
<div class="caption abs" style="left:732px;top:740px">Redesigning portfolio</div>
<div class="tile abs" style="left:908px;top:619px;width:140px;height:115px"><div role="img" aria-label="Photo of a child standing by a wall" style="background:linear-gradient(90deg,#d9dcdb,#e8eae9 50%,#bfc5c2)"></div></div>
<div class="caption abs" style="left:909px;top:740px">Redesigning portfolio</div>
<div class="tile abs" style="left:732px;top:769px;width:135px;height:117px"><div role="img" aria-label="Image of a chalkboard marketing strategy sketch" style="background:#2f5a48"></div></div>
<div class="caption abs" style="left:732px;top:893px">Redesigning portfolio</div>
<div class="tile abs" style="left:908px;top:769px;width:140px;height:116px"><div role="img" aria-label="Photo of wind turbines at sunset" style="background:linear-gradient(#3c6fc0,#8fb0de 60%,#e8c2a4 85%,#3a3f55)"></div></div>
<div class="caption abs" style="left:909px;top:893px">Redesigning portfolio</div>

<h2 class="pubs-title abs">Features Publiactaions</h2>
<ul class="pubs abs">
  <li><b>VIEWPOINTS</b> Managing technological discontinuities</li>
  <li><b>VIEWPOINTS</b> Global m-payments reports</li>
  <li><b>VIEWPOINTS</b> Major shake up in CEE TV markets</li>
  <li><b>PRESS Brenwick</b> Hale outlines the new face of innovation</li>
</ul>

<div class="dotted abs" style="left:113px;top:1130px;width:973px"></div>
<nav class="footer-links abs">Home - About Us - About Qianhai - Services - Portfolio - Partners - Our Team - Contact Us</nav>
<div class="copyright abs">Copyright (C) United Country . 2013.&nbsp; All Rights Reserved</div>

</body>
</html>
```